TVM8 Business Card Design Project

Design which catches the client with the first impression. A design which is professional and classy with elegance. We have also got another project running and the winning prize for that is $240 "tvm8 print + graphic design".
For all the company details please visit www.tvm8.com.
Please find the logo attached and i would like to have good colors for my business card.
, Design which catches the client with the first impression. A design which is professional and classy with elegance.
TVM8 is running two projects at the same time, please feel free to participate. The other project name is
Business

```html
<!DOCTYPE html>
<html lang="en">
<head>
<meta charset="utf-8">
<title>TVM8 Business Card</title>
<link rel="stylesheet" href="https://fonts.googleapis.com/css2?family=Roboto+Slab:wght@400;700&display=swap">
<style>
  :root {
    --backdrop: #d6d6d8;
    --ink: #111111;
    --lime: #a2cd3a;
    --teal: #3fb486;
    --stripe: #2fa97c;
    --text-dark: #1b1b1b;
    --social: #5a7fb0;
  }
  * { box-sizing: border-box; margin: 0; padding: 0; }
  html, body { width: 1200px; height: 900px; overflow: hidden; }
  body {
    background: var(--backdrop);
    font-family: "Roboto Slab", serif;
    position: relative;
  }
  .card {
    position: absolute;
    top: 300px;
    width: 520px;
    height: 300px;
    border-radius: 18px;
    overflow: hidden;
    box-shadow: 0 8px 24px rgba(0,0,0,0.18);
  }
  .card-front { left: 50px; background: var(--lime); }
  .card-back { left: 630px; background: var(--teal); }
  .front-wave { position: absolute; inset: 0; width: 100%; height: 100%; }

  .brand {
    position: absolute;
    display: flex;
    align-items: center;
    gap: 10px;
    font-weight: 700;
    line-height: 1;
  }
  .brand-dot { border-radius: 50%; display: block; }
  .front-brand { top: 36px; right: 36px; font-size: 44px; color: var(--stripe); }
  .front-brand .brand-dot { width: 22px; height: 22px; background: var(--stripe); }

  .social-links {
    position: absolute; top: 120px; left: 34px;
    display: flex; gap: 5px;
  }
  .social-links span {
    width: 17px; height: 17px; border-radius: 3px; background: var(--social); display: block;
  }

  .contact {
    position: absolute; top: 190px; left: 34px; color: var(--text-dark);
  }
  .contact-name { font-size: 17px; font-weight: 700; }
  .contact-role { font-size: 11px; margin-bottom: 14px; }
  .contact-lines { font-size: 11.5px; line-height: 1.55; list-style: none; }

  .divider {
    position: absolute; top: 190px; left: 300px; width: 1px; height: 56px; background: var(--text-dark); opacity: 0.6;
  }
  .address {
    position: absolute; top: 180px; left: 318px;
    font-size: 11.5px; line-height: 1.55; color: var(--text-dark); font-style: normal;
  }

  .back-brand {
    left: 60px; bottom: 80px; font-size: 64px; color: var(--ink);
  }
  .back-brand .brand-dot { width: 30px; height: 30px; background: var(--ink); }
  .back-url {
    position: absolute; left: 64px; bottom: 48px;
    font-size: 13px; letter-spacing: 0.55em; color: var(--ink);
  }
</style>
</head>
<body>
  <section class="card card-front" aria-label="Business card front">
    <svg class="front-wave" viewBox="0 0 520 300" aria-hidden="true">
      <path d="M0,0 H520 V70 C440,120 340,128 240,140 C150,150 70,168 0,205 Z" fill="var(--ink)"/>
      <path d="M0,213 C70,176 150,158 240,148 C340,136 440,128 520,78" fill="none" stroke="var(--stripe)" stroke-width="4"/>
    </svg>

    <div class="brand front-brand"><span class="brand-dot"></span>TVM8</div>

    <div class="social-links" aria-label="Social profiles">
      <span></span><span></span><span></span>
    </div>

    <div class="contact">
      <p class="contact-name">Daniel Morris</p>
      <p class="contact-role">Manager</p>
      <ul class="contact-lines">
        <li>p: 555.214.3098</li>
        <li>e: dmorris@tvm8.com</li>
        <li>w: www.tvm8.com</li>
      </ul>
    </div>

    <div class="divider"></div>

    <address class="address">
      48 Harbor Lane, Suite 12<br>
      Millbrook, CA 90210<br>
      WESTFIELD
    </address>
  </section>

  <section class="card card-back" aria-label="Business card back">
    <div class="brand back-brand"><span class="brand-dot"></span>TVM8</div>
    <p class="back-url">www.tvm8.com</p>
  </section>
</body>
</html>
```